A Recruitment Company Needs a Web Design that Expresses High Energy and Results

Our company, BrightLane Consultants, needs a web design for our recruiting business based in Asia (Taiwan). We provide recruitment services to many international companies. Our client base is as follows:
Hi-Tech - 60%
Healthcare and Consumer/FMCG - 15%
Industrial and Engineering - 15%
Banking and Finance - 10%

The website will be accessed by both clients and job seekers. As such, it should look professional, user-friendly and is interactive.

Industry/Entity Type

Business

Coding

Coded - Design and coding required

Number of Pages Required

5+ page

Font styles to use
Sans Serif

Colors
add136
ffffff
000000

Requirements
Must have
• Attached is the company's logo. the design mus be in line with it.

```html
<!DOCTYPE html>
<html lang="en">
<head>
<meta charset="utf-8">
<title>BrightLane Consultants</title>
<link href="https://fonts.googleapis.com/css2?family=Open+Sans:ital,wght@0,400;0,600;0,700;1,400&family=Oswald:wght@500&display=swap" rel="stylesheet">
<style>
:root{
  --lime:#add136;
  --lime-dark:#8fb327;
  --green:#2f9a3f;
  --ink:#2b2b2b;
  --text:#555;
  --bg:#f5f5f5;
  --white:#ffffff;
  --black:#000000;
  --nav-top:#4b4b4b;
  --nav-bottom:#2a2a2a;
}
*{margin:0;padding:0;box-sizing:border-box}
html,body{width:1200px;height:2459px;overflow:hidden}
body{background:var(--bg);font-family:"Open Sans",Arial,sans-serif;color:var(--text);position:relative}
.abs{position:absolute}
.top-bar{left:0;top:0;width:1200px;height:7px;background:var(--lime)}
.brand{left:85px;top:38px;line-height:1}
.brand-name{font-size:40px;font-weight:700;color:var(--green);letter-spacing:-1px;display:flex;align-items:center;gap:10px}
.brand-dot{width:22px;height:22px;border-radius:50%;background:var(--lime)}
.brand-sub{font-size:11px;letter-spacing:4px;color:var(--ink);margin-left:120px;margin-top:2px}
.search-input{left:767px;top:44px;width:225px;height:35px;background:var(--white);border:2px solid #ddd;font-size:10px;color:#999;padding:9px 10px}
.search-btn{left:1005px;top:44px;width:108px;height:35px;background:linear-gradient(var(--lime),var(--lime-dark));color:var(--white);font-size:11px;text-align:center;line-height:35px}
.main-nav{left:85px;top:116px;width:1030px;height:68px;background:linear-gradient(var(--nav-top),var(--nav-bottom));border-radius:6px 6px 0 0;display:flex;align-items:center;overflow:hidden}
.main-nav a{color:var(--white);font-size:13px;font-weight:600;text-decoration:none;padding:0 25px;height:68px;line-height:68px}
.main-nav a.active{background:linear-gradient(var(--lime),var(--lime-dark));width:125px;text-align:center;padding:0;margin-right:0}
.hero{left:85px;top:197px;width:1030px;height:526px;background:linear-gradient(90deg,#d9dde2,#eef0f3 45%,#cfd6dd)}
.hero-caption{left:170px;top:410px;font-size:33px;color:var(--white);line-height:41px;text-shadow:0 1px 3px rgba(0,0,0,.4)}
.hero-arrow{top:437px;width:32px;height:32px;border-radius:50%;background:var(--white)}
.hero-dots{left:555px;top:705px;width:110px;height:18px;background:var(--bg);border-radius:10px 10px 0 0;display:flex;justify-content:center;gap:5px;padding-top:5px}
.hero-dots span{width:9px;height:9px;border-radius:50%;background:#ccc}
.hero-dots span.on{background:var(--lime)}
.section-title{font-size:33px;color:var(--ink);font-weight:400}
.section-title em{font-style:normal;color:var(--green)}
.welcome-title{left:85px;top:756px}
.welcome-text{left:85px;top:800px;width:595px;font-size:12.5px;line-height:25.7px;text-align:justify}
.btn-more{left:85px;top:998px;width:117px;height:33px;background:linear-gradient(var(--lime),var(--lime-dark));color:var(--white);font-size:9px;font-weight:700;text-align:center;line-height:33px;border-radius:3px}
.welcome-photo{left:708px;top:757px;width:407px;height:261px;border:1px solid #ddd;background:var(--white);padding:6px}
.welcome-photo div{width:100%;height:100%;background:linear-gradient(#2f5f93,#9cc3e6 60%,#3f6e9e)}
.divider{left:85px;top:1051px;width:1012px;height:1px;background:#e0e0e0}
.services-title{left:83px;top:1072px}
.service{top:1139px;width:328px}
.service-photo{height:208px}
.service h3{font-size:17px;font-weight:600;color:var(--ink);margin-top:16px}
.service p{font-size:11.5px;line-height:20.5px;margin-top:6px;text-align:justify}
.service .link{font-size:11px;color:var(--green);margin-top:4px}
.client-title{left:83px;top:1516px}
.stat{top:1598px;width:190px;text-align:center}
.stat-value{left:0;top:0;width:184px;height:184px;display:flex;align-items:center;justify-content:center;font-family:"Oswald",sans-serif;font-size:50px;color:var(--green);position:absolute}
.stat-label{position:absolute;top:204px;left:-20px;width:224px;font-size:21px;color:var(--ink);line-height:31px}
.news-title{left:85px;top:1932px;font-size:27px}
.news-rule{left:85px;top:1982px;width:641px;height:1px;background:#ddd}
.news{left:85px;width:641px;display:flex;gap:24px}
.news-photo{width:161px;height:111px;flex:none;background:linear-gradient(#cfe2f2,#7fa8cc)}
.news h4{font-size:12.5px;font-weight:400;color:var(--ink);margin-top:8px}
.news .date{font-size:12.5px;color:var(--green);margin-top:8px}
.news p{font-size:11px;line-height:20px;margin-top:4px}
.testi-title{left:793px;top:1932px;font-size:27px;color:var(--green)}
.testi-box{left:798px;top:1990px;width:302px;height:236px;background:var(--lime);color:var(--white);font-style:italic;font-size:11px;line-height:21px;padding:30px 24px}
.testi-box .q{position:absolute;font-size:18px;font-style:normal}
.avatar{left:913px;top:2193px;width:62px;height:62px;border-radius:50%;border:3px solid var(--white);background:linear-gradient(#c7d7e6,#6c8aa6)}
.testi-name{left:880px;top:2258px;width:128px;text-align:center;font-size:11px;font-style:italic;color:var(--ink)}
.footer{left:0;top:2318px;width:1200px;height:141px;background:var(--black)}
.copyright{left:85px;top:2379px;font-size:15px;color:var(--white)}
.social{top:2375px;width:30px;height:30px}
</style>
</head>
<body>
<div class="abs top-bar"></div>

<header>
  <div class="abs brand">
    <div class="brand-name"><span class="brand-dot"></span>BrightLane</div>
    <div class="brand-sub">CONSULTANTS</div>
  </div>
  <div class="abs search-input">search this website...</div>
  <div class="abs search-btn">SEARCH</div>
  <nav class="abs main-nav">
    <a class="active" href="#">HOME</a>
    <a href="#">ABOUT US</a>
    <a href="#">CORPORATE</a>
    <a href="#">INDUSTRY</a>
    <a href="#">JOB SEEKERS</a>
    <a href="#">POST RESUME</a>
    <a href="#">CURRENT OPENINGS</a>
    <a href="#">CONTACT US</a>
  </nav>
</header>

<section>
  <div class="abs hero" role="img" aria-label="Photo of a businesswoman with two engineers in hard hats in a bright office"></div>
  <div class="abs hero-caption">We provide recruitment services to many<br>international companies</div>
  <div class="abs hero-arrow" style="left:112px"><svg width="32" height="32"><path d="M19 10l-6 6 6 6" fill="none" stroke="#999" stroke-width="2"/></svg></div>
  <div class="abs hero-arrow" style="left:1051px"><svg width="32" height="32"><path d="M13 10l6 6-6 6" fill="none" stroke="#999" stroke-width="2"/></svg></div>
  <div class="abs hero-dots"><span class="on"></span><span></span><span></span></div>
</section>

<section>
  <h2 class="abs section-title welcome-title"><em>Welcome To</em> BrightLane Consultancy</h2>
  <p class="abs welcome-text">Lorem ipsum dolor sit amet, consectetuer adipiscing elit, sed diam nonummy nibh euismod tincidunt ut laoreet dolore magna aliquam erat volutpat. Ut wisi enim ad minim veniam, quis nostrud exerci tation ullamcorper suscipit lobortis nisl ut aliquip ex ea commodo consequat. Duis autem vel eum iriure dolor in hendrerit in vulputate velit esse molestie consequat, vel illum dolore eu feugiat nulla facilisis at vero eros et accumsan et iusto odio dignissim qui blandit praesent luptatum zzril delenit augue duis dolore te feugait nulla facilisi. Lorem ipsum dolor sit amet, consectetuer adipiscing elit, sed diam nonummy nibh euismod tincidunt ut laoreet dolore magna aliquam erat volutpat.</p>
  <div class="abs btn-more">READ MORE</div>
  <div class="abs welcome-photo"><div role="img" aria-label="Silhouettes of business people walking in a bright glass corridor"></div></div>
  <div class="abs divider"></div>
</section>

<section>
  <h2 class="abs section-title services-title"><em>Our</em> Services</h2>
  <div class="abs service" style="left:85px">
    <div class="service-photo" role="img" aria-label="Business team meeting around a table" style="background:linear-gradient(#e8ecef,#9aa6b0)"></div>
    <h3>Corporate</h3>
    <p>Lorem ipsum dolor sit amet, consectetuer adipiscing elit, sed diam nonummy nibh euismod tincidunt ut laoreet dolore magna aliquam erat volutpat.</p>
    <div class="link">Read more +</div>
  </div>
  <div class="abs service" style="left:436px">
    <div class="service-photo" role="img" aria-label="Group of business people standing before a world map" style="background:linear-gradient(#3c4450,#171b22)"></div>
    <h3>Job Seekers</h3>
    <p>Lorem ipsum dolor sit amet, consectetuer adipiscing elit, sed diam nonummy nibh euismod tincidunt ut laoreet dolore magna aliquam erat volutpat.</p>
    <div class="link">Read more +</div>
  </div>
  <div class="abs service" style="left:787px">
    <div class="service-photo" role="img" aria-label="People facing a chalkboard of growth sketches and a bright doorway" style="background:linear-gradient(#4a4a4a,#2a2a2a)"></div>
    <h3>Industry</h3>
    <p>Lorem ipsum dolor sit amet, consectetuer adipiscing elit, sed diam nonummy nibh euismod tincidunt ut laoreet dolore magna aliquam erat volutpat.</p>
    <div class="link">Read more +</div>
  </div>
</section>

<section>
  <h2 class="abs section-title client-title"><em>Our</em> Client</h2>
  <div class="abs stat" style="left:139px">
    <svg class="abs" style="left:0;top:0" width="184" height="184"><circle cx="92" cy="92" r="85" fill="none" stroke="#add136" stroke-width="13"/><circle cx="92" cy="92" r="85" fill="none" stroke="#2f9a3f" stroke-width="13" stroke-dasharray="32 534" transform="rotate(90 92 92)"/></svg>
    <div class="stat-value">6%</div>
    <div class="stat-label">Hi-Tech</div>
  </div>
  <div class="abs stat" style="left:382px">
    <svg class="abs" style="left:0;top:0" width="184" height="184"><circle cx="92" cy="92" r="85" fill="none" stroke="#add136" stroke-width="13"/><circle cx="92" cy="92" r="85" fill="none" stroke="#2f9a3f" stroke-width="13" stroke-dasharray="80 534" transform="rotate(90 92 92)"/></svg>
    <div class="stat-value">15%</div>
    <div class="stat-label">Healthcare &amp;<br>Consumer/FMCG</div>
  </div>
  <div class="abs stat" style="left:623px">
    <svg class="abs" style="left:0;top:0" width="184" height="184"><circle cx="92" cy="92" r="85" fill="none" stroke="#add136" stroke-width="13"/><circle cx="92" cy="92" r="85" fill="none" stroke="#2f9a3f" stroke-width="13" stroke-dasharray="80 534" transform="rotate(90 92 92)"/></svg>
    <div class="stat-value">15%</div>
    <div class="stat-label">Industrial &amp;<br>Engineering</div>
  </div>
  <div class="abs stat" style="left:864px">
    <svg class="abs" style="left:0;top:0" width="184" height="184"><circle cx="92" cy="92" r="85" fill="none" stroke="#add136" stroke-width="13"/><circle cx="92" cy="92" r="85" fill="none" stroke="#2f9a3f" stroke-width="13" stroke-dasharray="80 534" transform="rotate(90 92 92)"/></svg>
    <div class="stat-value">15%</div>
    <div class="stat-label">Banking &amp; Finance</div>
  </div>
</section>

<section>
  <h2 class="abs section-title news-title"><em>Latest</em> News</h2>
  <div class="abs news-rule"></div>
  <article class="abs news" style="top:2003px">
    <div class="news-photo" role="img" aria-label="Two businessmen reviewing documents"></div>
    <div>
      <h4>SED UT PERSPICIATIS UNDE OMNIS</h4>
      <div class="date">22 - FEB - 2015</div>
      <p>Lorem ipsum dolor sit amet, consectetuer adipiscing elit, sed diam nonummy nibh euismod tincidunt ut laoreet dolore magna aliquam erat volutpat. Ut wisi enim ad minim veniam, quis nostrud</p>
    </div>
  </article>
  <article class="abs news" style="top:2152px">
    <div class="news-photo" role="img" aria-label="Team gathered in a bright office meeting"></div>
    <div>
      <h4>SED UT PERSPICIATIS UNDE OMNIS</h4>
      <div class="date">22 - FEB - 2015</div>
      <p>Lorem ipsum dolor sit amet, consectetuer adipiscing elit, sed diam nonummy nibh euismod tincidunt ut laoreet dolore magna aliquam erat volutpat. Ut wisi enim ad minim veniam, quis nostrud</p>
    </div>
  </article>

  <h2 class="abs section-title testi-title">Testimonials</h2>
  <div class="abs testi-box">
    <span class="q" style="left:12px;top:10px">&ldquo;</span>
    Lorem ipsum dolor sit amet, consectetuer adipiscing elit, sed diam nonummy nibh euismod tincidunt ut laoreet dolore magna aliquam erat volutpat. Ut wisi enim ad minim veniam, quis nostrud Lorem ipsum dolor sit amet, consectetuer adipiscing elit, sed diam nonummy nibh euismod tincidunt ut laoreet dolore magna aliquam erat volutpat.
    <span class="q" style="right:14px;top:200px">&rdquo;</span>
  </div>
  <div class="abs avatar" role="img" aria-label="Portrait of the client giving the testimonial"></div>
  <div class="abs testi-name">Mark Delaney</div>
</section>

<footer>
  <div class="abs footer"></div>
  <div class="abs copyright">© 2015 BrightLane &nbsp;All Rights Reserved</div>
  <div class="abs social" style="left:932px;background:#3b5998"></div>
  <div class="abs social" style="left:980px;background:#1da1d8"></div>
  <div class="abs social" style="left:1029px;background:#d8d8d8"></div>
  <div class="abs social" style="left:1078px;background:#1a7bb5"></div>
</footer>
</body>
</html>
```